Plakate für einen Immobilienmakler
Zielgruppe
Briefing für Plakatgestaltung – Immobilienvermietung
Ziel des Plakats:
Ich bin Immobilienmakler und benötige ein aussagekräftiges, aufmerksamkeitsstarkes Plakat zur Vermietung einer Immobilie. Das Plakat wird direkt in der zu vermietenden Immobilie angebracht und soll auf einen Blick klar machen, dass die Fläche zur Miete steht – idealerweise mit der Aussage: “Zu vermieten” oder “Fläche zu mieten” in den Fokus gesetzt.
Format und Einsatzort:
Das Objekt verfügt über drei sehr große Schaufenster (je ca. 3 x 4 Meter). Die Plakate werden in diese Fenster gehängt und sollen sowohl von der Straße aus gut lesbar sein als auch optisch professionell und hochwertig wirken. Wichtig ist, dass die Gestaltung auch aus einiger Entfernung (z. B. von gegenüberliegenden Straßenseiten) klar verständlich bleibt.
Stil und Designvorgaben:
Ich habe in der Vergangenheit bereits Werbematerialien für meine Marke verwendet (diese Plakate, Grafiken und Anzeigen füge ich dem Auftrag bei). Diese sollen als stilistische Orientierung dienen. Gerne darf das Design leicht weiterentwickelt werden, aber der Wiedererkennungswert meiner Marke soll erhalten bleiben.
Folgende Elemente sollen integriert werden:
• Mein Logo (wird als Datei bereitgestellt)
• Ein Porträtbild von mir (wird mitgeliefert)
• Klar erkennbare Kontaktinformationen (Telefon, Website, ggf. QR-Code)
• Auf Wunsch auch ein Call-to-Action, wie z. B. „Jetzt Besichtigung anfragen!“ oder „Kontaktieren Sie mich direkt!“
Optional – je nach Platz:
• Ein Bild der Immobilie oder ein Hinweis auf die Art der Fläche (z. B. “Gewerbefläche”, “Ladenfläche”, “Bürofläche”)
• Kurztext mit Details wie Größe, Lage oder Bezugstermin
Wichtig:
Das Hauptziel ist es, die Passanten direkt zu informieren: Diese Immobilie steht zur Miete – und ich bin der Ansprechpartner. Bitte darauf achten, dass die W..
Aufgabenstellung
Mein Logo soll dirn sein es soll klar sein und die Kunden sollen leicht meine Adresse scannen können oder abschreiben

```html
<!DOCTYPE html>
<html lang="de">
<head>
<meta charset="utf-8">
<title>Zu Vermieten – Plakat</title>
<link rel="stylesheet" href="https://fonts.googleapis.com/css2?family=Inter:wght@400;500;600;800&display=swap">
<style>
  :root {
    --backdrop: #e6e6e6;
    --paper: #ffffff;
    --ink: #111111;
    --ink-soft: #3a3a3a;
    --headline: #ffffff;
    --photo-top: #d8d3cc;
    --photo-mid: #a9a39b;
    --photo-bottom: #4b4d52;
  }
  * { margin: 0; padding: 0; box-sizing: border-box; }
  html, body {
    width: 1200px;
    height: 900px;
    overflow: hidden;
    background: var(--backdrop);
    font-family: "Inter", Arial, sans-serif;
    color: var(--ink);
  }
  .poster {
    position: absolute;
    left: 300px;
    top: 20px;
    width: 600px;
    height: 860px;
    background: var(--paper);
    overflow: hidden;
  }
  .hero-photo {
    position: absolute;
    left: 0;
    top: 0;
    width: 600px;
    height: 588px;
    background:
      radial-gradient(ellipse 180px 260px at 350px 330px, rgba(30,40,65,0.55), rgba(30,40,65,0) 100%),
      linear-gradient(180deg, var(--photo-top) 0%, var(--photo-mid) 55%, var(--photo-bottom) 100%);
  }
  .side-label {
    position: absolute;
    right: 18px;
    top: 36px;
    writing-mode: vertical-rl;
    font-size: 15px;
    font-weight: 500;
    color: var(--headline);
    letter-spacing: 0.5px;
  }
  .headline {
    position: absolute;
    left: 22px;
    top: 388px;
    color: var(--headline);
    font-weight: 800;
    line-height: 0.9;
    letter-spacing: -3px;
  }
  .headline .small { display: block; font-size: 82px; }
  .headline .large { display: block; font-size: 104px; }
  .brand {
    position: absolute;
    left: 26px;
    top: 622px;
    display: flex;
    align-items: center;
    gap: 8px;
    font-size: 17px;
    font-weight: 600;
    color: var(--ink);
  }
  .brand-mark {
    width: 14px;
    height: 14px;
    background: var(--ink);
  }
  .contact {
    position: absolute;
    left: 26px;
    top: 764px;
  }
  .contact-label { font-size: 10px; font-weight: 600; margin-bottom: 4px; }
  .contact-phone { font-size: 21px; font-weight: 500; letter-spacing: 0.3px; }
  .address {
    position: absolute;
    left: 26px;
    top: 825px;
    font-size: 10px;
    color: var(--ink-soft);
  }
  .cta {
    position: absolute;
    left: 336px;
    top: 752px;
    font-size: 22px;
    font-weight: 500;
    line-height: 1.15;
  }
  .cta-note {
    position: absolute;
    left: 336px;
    top: 825px;
    font-size: 10px;
    color: var(--ink-soft);
  }
</style>
</head>
<body>
  <div class="poster">
    <div class="hero-photo" role="img" aria-label="Porträt der Maklerin im Blazer mit verschränkten Armen vor einer hellen, möblierten Wohnung"></div>
    <div class="side-label">Mietfläche verfügbar</div>
    <h1 class="headline"><span class="small">zu</span><span class="large">Vermieten</span></h1>

    <div class="brand"><span class="brand-mark"></span><span>Halden Immobilien</span></div>

    <div class="contact">
      <p class="contact-label">Persönlicher Kontakt</p>
      <p class="contact-phone">0421 558 2190</p>
    </div>
    <p class="address">Büro Bremen · Lindenweg 14, 28195</p>

    <p class="cta">Jetzt besichtigung<br>anfragen!</p>
    <p class="cta-note">Gerne auch kurzfristig</p>
  </div>
</body>
</html>
```